Pricing Page; Request Quote Page Design

I'm looking to update our pricing page and request page to something more modern in terms of the layout/form design and with more content, but needs to be consistent with the rest of our site. I need two pages designed. 1) A general pricing page w/ CTAs for quotes, and 2) The request quote page with form. Ideally there would be (3) parts for our different packages (Express, Professional, Enterprise) on the pricing page, with CTAs on each section. I like the hero image approach used here https://plovane.com/pricing and here http://www.gridmarrow.com/wp-content/uploads/2016/08/corvalink-pricing-page-design.png In terms of the form page, mainly just looking for an improvement over this https://www.lumadrift.com/price-quote-request

I also included a sample mockup to provide a BIT of guidance, but looking for something a little different and modern.

Industry/Entity Type

Pricing

Number of Pages Required

2 page

Font styles to use
Sans Serif

Requirements
Must have
• Hero background image on main pricing page. Needs to follow the look and feel of lumadrift.com

```html
<!DOCTYPE html>
<html lang="en">
<head>
<meta charset="utf-8">
<title>Lumadrift — Pricing</title>
<link href="https://fonts.googleapis.com/css2?family=Raleway:wght@300;400;500&display=swap" rel="stylesheet">
<style>
:root{
  --header-bg: rgba(38,40,44,0.78);
  --accent: #8cd23c;
  --accent-dark: #72b82a;
  --ink: #222;
  --body-ink: #333;
  --card-bg: rgba(238,238,238,0.93);
  --express-top: #0b5fcc;
  --express-bottom: #0a3785;
  --pro-top: #0aa0a6;
  --pro-bottom: #06676d;
  --ent-top: #1c9c26;
  --ent-bottom: #0d6312;
  --white: #fff;
}
*{margin:0;padding:0;box-sizing:border-box}
html,body{width:1200px;height:764px;overflow:hidden}
body{font-family:"Raleway",sans-serif;color:var(--ink);position:relative}
.hero-photo{position:absolute;inset:0;
  background:
    radial-gradient(ellipse at 20% 30%, rgba(200,170,130,.55), transparent 60%),
    radial-gradient(ellipse at 80% 70%, rgba(150,120,100,.5), transparent 60%),
    linear-gradient(135deg,#cdb597 0%,#b69b80 45%,#a79a92 100%);}
.hero-veil{position:absolute;inset:0;background:rgba(235,230,222,.45)}
.site-header{position:absolute;top:0;left:0;width:1200px;height:80px;background:var(--header-bg)}
.brand{position:absolute;left:134px;top:31px;display:flex;align-items:center;gap:10px;color:var(--white);font-size:14px;font-weight:500;letter-spacing:9px}
.brand-mark{width:14px;height:14px;background:var(--white)}
.call{position:absolute;left:820px;top:20px;color:var(--white);font-size:11.5px}
.header-cta{position:absolute;left:945px;top:10px;width:122px;height:28px;background:var(--accent);color:var(--white);font-size:11.5px;display:flex;align-items:center;justify-content:center}
.main-nav{position:absolute;top:51px;left:0;width:1200px;font-size:11.5px;color:var(--white)}
.main-nav span{position:absolute;white-space:nowrap}
.main-nav .active{color:var(--accent)}
.hero-title{position:absolute;top:126px;left:0;width:1200px;text-align:center;font-weight:400;font-size:40px;color:#1e1e1e}
.hero-intro{position:absolute;top:192px;left:0;width:1200px;text-align:center;font-size:14.5px;line-height:24px;color:#1e1e1e}
.plan{position:absolute;top:296px;width:290px;height:392px;background:var(--card-bg)}
.plan-head{height:67px;display:flex;align-items:center;justify-content:center;color:var(--white);font-size:24px;font-weight:400}
.express .plan-head{background:linear-gradient(var(--express-top),var(--express-bottom))}
.professional .plan-head{background:linear-gradient(var(--pro-top),var(--pro-bottom))}
.enterprise .plan-head{background:linear-gradient(var(--ent-top),var(--ent-bottom))}
.plan-copy{position:absolute;left:10px;right:10px;text-align:center;font-size:14px;line-height:33.6px;color:var(--body-ink)}
.plan-cta{position:absolute;left:55px;top:314px;width:184px;height:46px;background:linear-gradient(var(--accent),var(--accent-dark));color:var(--white);font-size:13.5px;font-weight:500;display:flex;align-items:center;justify-content:center;text-shadow:0 1px 2px rgba(0,0,0,.45);border-radius:2px}
.site-footer{position:absolute;top:725px;left:134px;font-size:11px;color:var(--ink)}
.site-footer .sep{margin:0 8px}
.social{position:absolute;top:718px;left:914px;display:flex;gap:28px}
.social span{width:20px;height:20px;border-radius:50%;background:#1b1b1b;display:block}
</style>
</head>
<body>
<div class="hero-photo" role="img" aria-label="Overhead photo of a team working around a wooden table with laptops, notebooks and coffee"></div>
<div class="hero-veil"></div>

<header class="site-header">
  <div class="brand"><span class="brand-mark"></span>LUMADRIFT</div>
  <div class="call">CALL 1-866-555-0142</div>
  <div class="header-cta">REQUEST QUOTE</div>
  <nav class="main-nav">
    <span class="active" style="left:556px">FEATURES</span>
    <span style="left:641px">SERVICES</span>
    <span style="left:722px">PRICING</span>
    <span style="left:797px">RESOURCES</span>
    <span style="left:891px">BLOG</span>
    <span style="left:954px">NEWS</span>
    <span style="left:1017px">CONTACT</span>
  </nav>
</header>

<h1 class="hero-title">Flexible Pricing Designed to Fit Your Business</h1>
<p class="hero-intro">Our pay-as-you-grow pricing model is geared to minimize risk and maximize return.<br>Whether launching a new learning initiative, or looking to migrate (or integrate) an<br>existing business with our Learning Business Platform, we have you covered.</p>

<section class="plan express" style="left:132px">
  <div class="plan-head">EXPRESS</div>
  <p class="plan-copy" style="top:99px">Launch in weeks,<br>not months. Perfect for smaller<br>businesses with less than 1,000 users<br>and requiring less than 25 courses.<br>Packages start at $499.</p>
  <div class="plan-cta">REQUEST QUOTE</div>
</section>

<section class="plan professional" style="left:455px">
  <div class="plan-head">PROFESSIONAL</div>
  <p class="plan-copy" style="top:110px">Designed for moreestablished<br>learningbusinesses which are need to<br>scale andleverage moderntechnology.<br>Up to 10kusers &amp; 100 courses.</p>
  <div class="plan-cta">REQUEST QUOTE</div>
</section>

<section class="plan enterprise" style="left:778px">
  <div class="plan-head">ENTERPRISE</div>
  <p class="plan-copy" style="top:115px">For larger organizationsneeding to<br>scale learning globally to more than<br>10,000 users, with hundreds of<br>courses and multiple instances.</p>
  <div class="plan-cta">REQUEST QUOTE</div>
</section>

<footer class="site-footer">Copyright © 2016 Lumadrift, Inc.<span class="sep">|</span>Privacy Policy</footer>
<div class="social" aria-label="Social links">
  <span aria-label="Social link"></span>
  <span aria-label="Social link"></span>
  <span aria-label="Social link"></span>
  <span aria-label="Social link"></span>
</div>
</body>
</html>
```